Harborview Sight Fellowship Hall needs an ad/flyer for convention program

Established in 1949, the Harborview Sight Fellowship Hall's mission is to enrich the lives of blind and visually impaired adults by preparing them for a normal, active life in a society that is principally sighted by encouraging independence.

Located in Quillmont Green in San Diego, California, we are a nonprofit that gives blind and visually impaired people in our community an opportunity to socialize and interact. We help members build skills, confidence, and self-esteem through our various social, recreational, and educational activities. We were founded partially by Otter Society members and receive ongoing funding from them.

We need an 8 1/2 by 11 inch color ad in jpg format. We would like it to be editable. This will be the foundation of our rebranding. The ad will be in a meeting program of the California Otters (californiaotters-example.org) with the goal of highlighting some of our programs in order to solicit donations from individual Otter Societies, preferably ongoing ones.

We would like the ad to be generic enough that we can use the ad for other events and as a flyer in the future. We want the ad/flyer to be classic but eye popping with color. We want the design to reflect a professional and lively organization that loves to serve our members. We don’t entirely love our logo, but it’s what we have for now. Our next task will be a new logo design.

We would like to highlight some of our programs for our members include bingo, blind waterskiing and surfing, cooking and ceramic classes, foreign language classes, self defense classes, yoga, and craft classes. Many of the crafts our members make are sold during fundraisers, and they include blankets, scarves, beaded animals, and more. See a sampling of pictures. We provide transportation to and from our Center, free lunch while at the Center, and food to take home. Many of these activities continue during the pandemic via online platforms. We are doing monthly home deliveries of food to our members.

We need donations to keep our programs going, and we have building repairs & maintenance that we need donations in order to complete. See attached document regarding donations. Please reach out if you have questions. Thank you.

Web address: hvsfh-example.org
Street address: The Harborview Sight Fellowship Hall, 4472 Marrow Ln San Diego, CA 92188
Email address: donation@hvsfh-example.org
To make a donation: https://hvsfh-example.org/donate-2/

Target Market(s)

Donors

Industry/Entity Type

NonProfit

Font styles to use
Sans Serif

Requirements
Must have
• Highlight programs and information on how to make a donation.
Nice to have
• Information on how much each dollar donated will go - see attachment
Should not have
• Unprofessional or sloppy details

```html
<!DOCTYPE html>
<html lang="en">
<head>
<meta charset="utf-8">
<title>Harborview Sight Fellowship Hall – Donation Flyer</title>
<link href="https://fonts.googleapis.com/css2?family=Montserrat:wght@300;400;600;700&family=Tinos:wght@400;700&display=swap" rel="stylesheet">
<style>
  :root {
    --ink: #222222;
    --band: #262626;
    --paper: #ffffff;
    --muted: #c4c4c4;
    --text: #2b2b2b;
    --skyline: #ececec;
    --knit-purple: #7f6aa8;
    --knit-pink: #f0b7cb;
    --knit-teal: #7fc6c6;
    --knit-blue: #3d8fc6;
    --knit-coral: #e9777a;
  }
  * { box-sizing: border-box; margin: 0; padding: 0; }
  html, body { width: 800px; height: 1200px; overflow: hidden; background: var(--paper); }
  body { font-family: "Montserrat", sans-serif; color: var(--text); position: relative; }

  .serif { font-family: "Tinos", serif; }

  .skyline-band {
    position: absolute; left: 0; right: 0; bottom: 0; height: 150px;
    background: linear-gradient(to top, var(--skyline) 0%, #f4f4f4 60%, rgba(255,255,255,0) 100%);
  }

  .brand {
    position: absolute; left: 46px; top: 70px; width: 300px;
    display: flex; align-items: center; gap: 12px;
  }
  .brand-mark { width: 18px; height: 18px; background: var(--ink); flex: none; }
  .brand-name {
    font-family: "Tinos", serif; font-weight: 700; font-size: 26px; line-height: 1.1; color: var(--ink);
  }

  .know-band {
    position: absolute; left: 0; top: 196px; width: 382px; height: 80px;
    background: var(--band); color: #fff;
    font-family: "Tinos", serif; font-weight: 700; font-size: 36px;
    display: flex; align-items: center; padding-left: 50px; letter-spacing: 0.5px;
  }

  .facts { position: absolute; left: 48px; top: 306px; width: 330px; list-style: none; }
  .fact { display: flex; gap: 14px; margin-bottom: 20px; }
  .fact-num {
    font-weight: 300; font-size: 28px; line-height: 0.9; color: var(--muted); width: 34px; flex: none;
  }
  .fact-text { font-size: 10.8px; line-height: 1.32; }
  .fact-text b { font-weight: 700; }

  .gallery { position: absolute; left: 50px; top: 712px; width: 352px; height: 228px; display: flex; gap: 8px; }
  .photo { flex: 1; border: 3px solid #e2e2e2; }
  .photo-penguin { background: linear-gradient(160deg, #d9d9d9 0%, #5a5a5a 55%, #c9c9c9 100%); }
  .photo-angel { background: linear-gradient(180deg, #eeeeee 0%, #d8d8d8 45%, #2f4ea8 80%, #1c2f78 100%); }

  .lunch-box {
    position: absolute; left: 50px; top: 948px; width: 352px; height: 118px;
    background: var(--band); color: #fff; text-align: center;
    font-family: "Tinos", serif; font-size: 16px; line-height: 1.25; padding: 12px 16px;
  }
  .lunch-box hr { border: 0; border-top: 1px dashed #8a8a8a; margin: 9px 0 8px; }

  .knit-photo {
    position: absolute; left: 412px; top: 0; width: 388px; height: 646px;
    background:
      linear-gradient(180deg,
        var(--knit-purple) 0%, var(--knit-pink) 18%, var(--knit-pink) 32%,
        var(--knit-purple) 42%, var(--knit-coral) 55%, var(--knit-purple) 66%,
        var(--knit-blue) 84%, var(--knit-teal) 100%);
  }

  .precovid { position: absolute; left: 440px; top: 676px; width: 340px; }
  .precovid h2 { font-family: "Tinos", serif; font-weight: 700; font-size: 36px; color: var(--ink); margin-bottom: 8px; }
  .tier { margin-bottom: 11px; }
  .tier h3 { font-family: "Tinos", serif; font-weight: 700; font-size: 20px; color: var(--ink); margin-bottom: 4px; }
  .tier h3 sup { font-size: 11px; }
  .tier ul { list-style: none; }
  .tier li { display: flex; gap: 5px; font-size: 9.6px; line-height: 1.3; margin-bottom: 3px; }
  .tier li svg { flex: none; margin-top: 1px; }

  .contact { position: absolute; top: 1110px; font-size: 12.5px; line-height: 1.3; }
  .contact-address { left: 50px; width: 260px; display: flex; gap: 6px; }
  .contact-web { left: 320px; }
  .contact-web div { display: flex; gap: 8px; align-items: center; margin-bottom: 6px; }

  .donate { position: absolute; left: 535px; top: 1100px; width: 250px; border-left: 2px solid var(--ink); padding-left: 22px; }
  .donate-title { font-family: "Tinos", serif; font-weight: 700; font-size: 24px; color: var(--ink); white-space: nowrap; }
  .donate-url {
    display: inline-block; margin-top: 2px; background: var(--band); color: #fff;
    font-family: "Tinos", serif; font-size: 12.5px; padding: 3px 14px; border-radius: 12px; white-space: nowrap;
  }
</style>
</head>
<body>
  <div class="skyline-band" role="img" aria-label="Faint city skyline silhouette along the bottom edge"></div>

  <div class="brand">
    <span class="brand-mark"></span>
    <span class="brand-name">Harborview Sight Fellowship Hall</span>
  </div>

  <div class="know-band">DID YOU KNOW?</div>

  <ol class="facts">
    <li class="fact"><span class="fact-num">01</span><p class="fact-text">During the pandemic we offer Bingo, Trivia and other virtual games every week, where blind and low vision participants can win HVSFH bucks. <b>You can sponsor one day of games for $35.</b></p></li>
    <li class="fact"><span class="fact-num">02</span><p class="fact-text">You can provide 75 gift bags for our ‘We are in This Together’ home delivery program. Many of our blind and low vision people are isolated and stuck at home. These gift packages are welcomed with enthusiasm and gratefulness. Your rewards are huge smiles and happy faces.</p></li>
    <li class="fact"><span class="fact-num">03</span><p class="fact-text">Our building is over 20 years old and requires ongoing maintenance and repairs</p></li>
    <li class="fact"><span class="fact-num">04</span><p class="fact-text"><b>Fencing (cage) required to protect outside air conditioning units from vandalism. Cost: $2,500</b></p></li>
    <li class="fact"><span class="fact-num">05</span><p class="fact-text">Wanted: Sponsors for weekly virtual bingo and trivia games: Blind and Low vision participants receive one HVSFH buck per win. HVSFH bucks are turned into gift cards and Bayline transportation passes. <b>Sponsor one week for $40. Sponsor 1 month for $160</b></p></li>
  </ol>

  <div class="gallery">
    <div class="photo photo-penguin" role="img" aria-label="Photo of a beaded penguin craft on a folded knit blanket"></div>
    <div class="photo photo-angel" role="img" aria-label="Photo of a beaded angel ornament with blue skirt"></div>
  </div>

  <div class="lunch-box">
    <p>$1,083 per month or $13,000 per year will fund our entire lunch program for the year.</p>
    <hr>
    <p>Every dollar donated goes to support HVSFH participants and programs.</p>
  </div>

  <div class="knit-photo" role="img" aria-label="Photo of a stack of colourful hand-knit blankets in purple, pink, coral, blue and teal with a handmade badge"></div>

  <section class="precovid">
    <h2>PRE-COVID</h2>
    <div class="tier">
      <h3><sup>$</sup>10 per month or <sup>$</sup>120 will buy:</h3>
      <ul>
        <li><svg width="10" height="10" viewBox="0 0 10 10"><circle cx="5" cy="5" r="5" fill="#333"/><path d="M2.6 5.2 4.3 6.8 7.4 3.4" stroke="#fff" stroke-width="1.3" fill="none"/></svg>60 meals for our lunch program – we serve 130 meals each week</li>
        <li><svg width="10" height="10" viewBox="0 0 10 10"><circle cx="5" cy="5" r="5" fill="#333"/><path d="M2.6 5.2 4.3 6.8 7.4 3.4" stroke="#fff" stroke-width="1.3" fill="none"/></svg>13 round trip Bayline transportation tickets</li>
        <li><svg width="10" height="10" viewBox="0 0 10 10"><circle cx="5" cy="5" r="5" fill="#333"/><path d="M2.6 5.2 4.3 6.8 7.4 3.4" stroke="#fff" stroke-width="1.3" fill="none"/></svg>Enough beads to make 35 Dottie Fern angels in our craft class</li>
      </ul>
    </div>
    <div class="tier">
      <h3><sup>$</sup>20 per month or <sup>$</sup>240 will buy:</h3>
      <ul>
        <li><svg width="10" height="10" viewBox="0 0 10 10"><circle cx="5" cy="5" r="5" fill="#333"/><path d="M2.6 5.2 4.3 6.8 7.4 3.4" stroke="#fff" stroke-width="1.3" fill="none"/></svg>26 round trip Bayline transportation tickets</li>
        <li><svg width="10" height="10" viewBox="0 0 10 10"><circle cx="5" cy="5" r="5" fill="#333"/><path d="M2.6 5.2 4.3 6.8 7.4 3.4" stroke="#fff" stroke-width="1.3" fill="none"/></svg>One month of large print and Braille translation newsletter printing</li>
      </ul>
    </div>
    <div class="tier">
      <h3><sup>$</sup>50 per month or <sup>$</sup>600 will buy:</h3>
      <ul>
        <li><svg width="10" height="10" viewBox="0 0 10 10"><circle cx="5" cy="5" r="5" fill="#333"/><path d="M2.6 5.2 4.3 6.8 7.4 3.4" stroke="#fff" stroke-width="1.3" fill="none"/></svg>300 lunches</li>
        <li><svg width="10" height="10" viewBox="0 0 10 10"><circle cx="5" cy="5" r="5" fill="#333"/><path d="M2.6 5.2 4.3 6.8 7.4 3.4" stroke="#fff" stroke-width="1.3" fill="none"/></svg>Thanksgiving dinner with all the fixings for 80 to 100 guests</li>
      </ul>
    </div>
    <div class="tier">
      <h3><sup>$</sup>100 per month or <sup>$</sup>1200 will buy:</h3>
      <ul>
        <li><svg width="10" height="10" viewBox="0 0 10 10"><circle cx="5" cy="5" r="5" fill="#333"/><path d="M2.6 5.2 4.3 6.8 7.4 3.4" stroke="#fff" stroke-width="1.3" fill="none"/></svg>Approximately 10 Bingo parties including food and prizes</li>
      </ul>
    </div>
  </section>

  <div class="contact contact-address">
    <svg width="11" height="15" viewBox="0 0 11 15"><path d="M5.5 0.8A4.6 4.6 0 0 0 0.9 5.4c0 3.4 4.6 8.8 4.6 8.8s4.6-5.4 4.6-8.8A4.6 4.6 0 0 0 5.5 0.8z" fill="none" stroke="#333" stroke-width="1.4"/><circle cx="5.5" cy="5.4" r="1.6" fill="#333"/></svg>
    <p>The Harborview Sight Fellowship Hall, 4472 Marrow Ln San Diego, CA 92188</p>
  </div>

  <div class="contact contact-web">
    <div><svg width="12" height="9" viewBox="0 0 12 9"><rect x="0.5" y="0.5" width="11" height="8" fill="#333"/><path d="M0.5 0.8 6 5 11.5 0.8" stroke="#fff" fill="none"/></svg><span>donation@hvsfh-example.org</span></div>
    <div><svg width="12" height="12" viewBox="0 0 12 12"><circle cx="6" cy="6" r="5.3" fill="none" stroke="#333" stroke-width="1.2"/><ellipse cx="6" cy="6" rx="2.3" ry="5.3" fill="none" stroke="#333"/><path d="M0.8 6h10.4" stroke="#333"/></svg><span>www.hvsfh-example.org</span></div>
  </div>

  <div class="donate">
    <div class="donate-title">To make a donation</div>
    <span class="donate-url">https://hvsfh-example.org/donate-2/</span>
  </div>
</body>
</html>
```